Modern and professional business card for medical weight management practice
Crestline Weight Management MD
Modern and professional business card for medical weight management practice - Health
Creative Brief
Professional
Tarlen Voskry M.D.
Medical Director
418 West Harlowe Court Suite B Sunnyvale, CA 94086
Will be provided
Crestlineweightcaremd@mailnest.example
Crestlineweightcaremd.example
Member of National Council of Metabolic Practice Member of United Academy of Clinical Associates Clinical Professor, PVMI Diplomate National council of Physicians
Have the appointment and the direction
Dravok Dravok
Please check private message.. Thanks.
brookvanehealth brookvanehealth
Hello Guys, Could you also include the following: Tarlen Voskry, M.D. Assistant Clinical Professor, PVMI Member of National Guild of Metabolic Clinicians
Hello guys, I have uploaded my new logo (Crestline Weight Management MD). Please forward me the designs. Thanks

```html
<!DOCTYPE html>
<html lang="en">
<head>
<meta charset="utf-8">
<title>Tarlen Voskry M.D. – Business Card</title>
<link rel="stylesheet" href="https://fonts.googleapis.com/css2?family=Arimo:wght@400;700&display=swap">
<style>
  :root {
    --backdrop: #e6e8ea;
    --card: #ffffff;
    --brand-blue: #19a3e8;
    --brand-blue-light: #6fcaf4;
    --swoosh-grey: #5e5b55;
    --ink: #2d2d2d;
    --ink-soft: #555555;
  }
  * { box-sizing: border-box; margin: 0; padding: 0; }
  html, body {
    width: 1200px;
    height: 780px;
    overflow: hidden;
    background: var(--backdrop);
    font-family: "Arimo", Arial, sans-serif;
  }
  .business-card {
    position: absolute;
    left: 60px;
    top: 80px;
    width: 1080px;
    height: 620px;
    background: var(--card);
    border-radius: 36px;
    overflow: hidden;
    box-shadow: 0 6px 24px rgba(0,0,0,0.15);
  }
  .card-waves {
    position: absolute;
    inset: 0;
    width: 100%;
    height: 100%;
  }
  .wave-blue { fill: var(--brand-blue); }
  .wave-highlight { fill: none; stroke: var(--brand-blue-light); stroke-width: 6; }
  .wave-grey { fill: var(--swoosh-grey); }

  .holder {
    position: absolute;
    right: 56px;
    top: 44px;
    text-align: right;
    color: #ffffff;
  }
  .holder-name { font-size: 34px; font-weight: 700; line-height: 1.2; }
  .holder-title { font-size: 21px; font-weight: 700; margin-top: 4px; }

  .brand {
    position: absolute;
    left: 56px;
    top: 470px;
    display: flex;
    align-items: center;
    gap: 22px;
  }
  .brand-mark {
    width: 86px;
    height: 86px;
    border-radius: 50%;
    background: var(--swoosh-grey);
  }
  .brand-name {
    font-size: 40px;
    font-weight: 400;
    color: var(--brand-blue);
    white-space: nowrap;
  }

  .contact {
    position: absolute;
    left: 540px;
    top: 290px;
    color: var(--ink);
    font-size: 19px;
  }
  .contact-address { line-height: 1.3; margin-bottom: 22px; }
  .contact-list { list-style: none; }
  .contact-list li {
    display: flex;
    align-items: center;
    gap: 12px;
    height: 32px;
  }
  .contact-icon { width: 20px; height: 20px; fill: var(--brand-blue); flex: none; }
  .contact-web { margin-top: 10px; line-height: 1.55; color: var(--ink-soft); }
</style>
</head>
<body>
  <article class="business-card">
    <svg class="card-waves" viewBox="0 0 1080 620" preserveAspectRatio="none" aria-hidden="true">
      <path class="wave-blue" d="M0 0 H1080 V125 C840 145 560 120 330 190 C180 236 70 300 0 340 Z"/>
      <path class="wave-highlight" d="M420 172 C640 118 880 132 1080 112"/>
      <path class="wave-grey" d="M0 440 C70 320 270 225 560 200 C340 250 150 330 22 470 Z"/>
    </svg>

    <header class="holder">
      <h1 class="holder-name">Tarlen Voskry M.D.</h1>
      <p class="holder-title">Medical Director</p>
    </header>

    <div class="brand">
      <span class="brand-mark"></span>
      <span class="brand-name">Brookvane Health</span>
    </div>

    <section class="contact">
      <address class="contact-address" style="font-style: normal;">
        418 West Harlowe Court<br>
        Suite B, Sunnyvale, CA 94086
      </address>
      <ul class="contact-list">
        <li>
          <svg class="contact-icon" viewBox="0 0 24 24" aria-label="Phone"><path d="M6.6 10.8a15.1 15.1 0 0 0 6.6 6.6l2.2-2.2a1 1 0 0 1 1-.25 11.4 11.4 0 0 0 3.6.6 1 1 0 0 1 1 1V20a1 1 0 0 1-1 1A17 17 0 0 1 3 4a1 1 0 0 1 1-1h3.5a1 1 0 0 1 1 1c0 1.25.2 2.45.6 3.6a1 1 0 0 1-.25 1z"/></svg>
          866-555-0142
        </li>
        <li>
          <svg class="contact-icon" viewBox="0 0 24 24" aria-label="Office phone"><path d="M6.6 10.8a15.1 15.1 0 0 0 6.6 6.6l2.2-2.2a1 1 0 0 1 1-.25 11.4 11.4 0 0 0 3.6.6 1 1 0 0 1 1 1V20a1 1 0 0 1-1 1A17 17 0 0 1 3 4a1 1 0 0 1 1-1h3.5a1 1 0 0 1 1 1c0 1.25.2 2.45.6 3.6a1 1 0 0 1-.25 1z"/></svg>
          408-555-0171
        </li>
        <li>
          <svg class="contact-icon" viewBox="0 0 24 24" aria-label="Mobile"><path d="M7 1h10a2 2 0 0 1 2 2v18a2 2 0 0 1-2 2H7a2 2 0 0 1-2-2V3a2 2 0 0 1 2-2zm0 3v14h10V4zm5 15.5a1.2 1.2 0 1 0 0 2.4 1.2 1.2 0 0 0 0-2.4z"/></svg>
          408-555-0125
        </li>
        <li>
          <svg class="contact-icon" viewBox="0 0 24 24" aria-label="Fax"><path d="M6 2h10l2 2v5H6zM4 10h16a2 2 0 0 1 2 2v7h-4v3H6v-3H2v-7a2 2 0 0 1 2-2zm4 6v4h8v-4z"/></svg>
          345 555 0198
        </li>
      </ul>
      <p class="contact-web">
        Crestlineweightcaremd@mailnest.example<br>
        Crestlineweightcaremd.example
      </p>
    </section>
  </article>
</body>
</html>
```